E-commerce website for interior joinery product - Pantrel Trade

we want to create a E-commerce website to list our modular products.
other than E-commerce functions, we will also require membership logins and setting different price tiers for B2B customers (construction company and home building groups. for logos and our products etc please visit www.pantrel.co.nz
You can also get some ideas from https://kovaclosets.co.nz/ready-to-order/

Number of Pages Required

5+ page

Requirements
Must have
• on the product page, the customer can have the option to choose different colours and upgradable options.

```html
<!DOCTYPE html>
<html lang="en">
<head>
<meta charset="utf-8">
<title>Melamine Sliding Doors – Pantrel</title>
<link href="https://fonts.googleapis.com/css2?family=Merriweather:wght@700&family=Open+Sans:wght@400;600;700&display=swap" rel="stylesheet">
<style>
:root{
  --green:#80c342;
  --ink:#3a3a3a;
  --text:#555a60;
  --muted:#8a8f94;
  --page:#f4f4f4;
  --card:#ffffff;
  --rule:#e6e6e6;
  --navy:#03182a;
  --foot:#f9f9f9;
  --teal:#5b7780;
}
*{margin:0;padding:0;box-sizing:border-box}
html,body{width:682px;height:1200px;overflow:hidden}
body{position:relative;background:var(--page);font-family:"Open Sans",sans-serif;color:var(--text)}
.abs{position:absolute}
.site-header{position:absolute;left:0;top:0;width:682px;height:41px;background:#fff;border-bottom:1px solid #ececec}
.brand{position:absolute;display:flex;align-items:center;gap:4px;font-family:"Open Sans",sans-serif;font-weight:600;color:var(--teal)}
.brand .mark{width:11px;height:11px;background:var(--teal)}
.nav{position:absolute;top:15px;font-size:7px;color:var(--ink);white-space:nowrap}
.nav .caret{font-size:5px;margin-left:2px}
.cart{position:absolute;left:578px;top:14px;width:11px;height:12px;border:1px solid var(--green);border-radius:1px;font-size:5px;color:var(--green);text-align:center;line-height:11px}
.product-card{position:absolute;left:85px;top:69px;width:512px;height:853px;background:var(--card)}
.photo{position:absolute;background:linear-gradient(90deg,#8d9598 0%,#3c3330 12%,#4a3f3b 50%,#3a312e 88%,#b8bcbe 100%)}
.photo.main{left:131px;top:105px;width:210px;height:315px;background:linear-gradient(180deg,#d9dcdc 0%,#8f9496 8%,#433935 15%,#4b403c 50%,#3a302d 80%,#9e9894 88%,#c4bebb 100%)}
.badge{position:absolute;width:24px;height:24px;border-radius:50%;background:var(--green);color:#fff;font-size:6.5px;text-align:center;line-height:24px}
.zoom{position:absolute;left:319px;top:112px;width:15px;height:15px;border-radius:50%;background:#fff}
.thumb{position:absolute;top:427px;width:47px;height:48px}
.crumb{position:absolute;left:358px;top:107px;font-size:6px;color:var(--muted)}
.title{position:absolute;left:358px;top:122px;font-family:"Merriweather",serif;font-weight:700;font-size:14px;color:var(--ink)}
.price{position:absolute;left:358px;top:147px;font-size:10.5px;color:var(--ink)}
.price del{color:var(--muted);margin-right:3px}
.opt-label{position:absolute;font-size:7px;font-weight:600;color:var(--ink)}
.opt-value{position:absolute;font-size:7px;color:var(--text)}
.opt-value .sep{margin:0 4px}
.qty{position:absolute;left:358px;top:349px;width:24px;height:14px;border:1px solid #ddd;font-size:6px;line-height:12px;padding-left:7px;color:var(--ink)}
.add-cart{position:absolute;left:385px;top:349px;width:68px;height:14px;border-radius:7px;background:var(--green);color:#fff;font-size:6.5px;font-weight:700;text-align:center;line-height:14px}
.rule{position:absolute;height:1px;background:var(--rule)}
.cats{position:absolute;left:358px;top:381px;font-size:6px;color:var(--ink)}
.cats a{color:var(--green);text-decoration:none}
.tab{position:absolute;top:501px;font-size:7px;font-weight:600;color:var(--ink)}
.tab-active{position:absolute;left:131px;top:495px;width:36px;height:1.5px;background:var(--green)}
.section-title{position:absolute;left:131px;top:701px;font-family:"Merriweather",serif;font-weight:700;font-size:12px;color:var(--ink)}
.related{position:absolute;top:723px;width:99px}
.related .img{width:99px;height:99px}
.related .cat{font-size:5.5px;color:var(--muted);margin-top:5px}
.related .name{font-family:"Merriweather",serif;font-weight:700;font-size:7px;color:var(--ink);margin-top:1px}
.related .stars{font-size:6px;color:var(--green);letter-spacing:-0.5px;margin-top:1px;line-height:8px}
.related .cost{font-size:6px;color:var(--ink);font-weight:600}
.related .cost del{color:var(--muted);font-weight:400;margin-right:2px}
.cta-band{position:absolute;left:0;top:949px;width:682px;height:76px;background:var(--navy)}
.cta-band h2{position:absolute;left:85px;top:29px;font-family:"Merriweather",serif;font-weight:700;font-size:12.5px;color:#fff}
.shop-now{position:absolute;left:434px;top:29px;width:78px;height:21px;border-radius:11px;background:var(--green);color:#fff;font-size:7px;font-weight:700;text-align:center;line-height:21px;letter-spacing:.3px}
.site-footer{position:absolute;left:0;top:1025px;width:682px;height:175px;background:var(--foot)}
.foot-head{position:absolute;top:1063px;font-size:8px;font-weight:600;letter-spacing:1px;color:#7a7f84;text-align:center;width:120px}
.foot-link{position:absolute;font-size:7px;color:var(--ink);text-align:center;width:120px}
.branch{position:absolute;left:473px;font-size:7px}
.branch.name{color:var(--ink);font-weight:600}
.branch.tel{color:var(--green)}
</style>
</head>
<body>

<header class="site-header">
  <div class="brand" style="left:94px;top:14px;font-size:12px"><span class="mark"></span>Pantrel</div>
  <span class="nav" style="left:373px">Home</span>
  <span class="nav" style="left:406px">Products<span class="caret">&#8964;</span></span>
  <span class="nav" style="left:456px">Gallery</span>
  <span class="nav" style="left:492px">Contact</span>
  <span class="nav" style="left:530px">Account<span class="caret">&#8964;</span></span>
  <span class="cart">0</span>
</header>

<main class="product-card"></main>

<div class="photo main" role="img" aria-label="Dark oak melamine sliding wardrobe doors with a frosted glass band, set in a white alcove"></div>
<span class="badge" style="left:134px;top:108px">Sale!</span>
<span class="zoom"><svg width="15" height="15" viewBox="0 0 15 15"><circle cx="6.8" cy="6.8" r="2.6" fill="none" stroke="#222" stroke-width="1"/><line x1="8.7" y1="8.7" x2="10.5" y2="10.5" stroke="#222" stroke-width="1.2"/></svg></span>

<div class="thumb" style="left:131px;background:linear-gradient(90deg,#3c322f,#4d423e 48%,#b9bdbf 50%,#3f3532)" role="img" aria-label="Dark oak door thumbnail"></div>
<div class="thumb" style="left:185px;background:linear-gradient(90deg,#eceae6,#d8d3cc 60%,#9aa6ad 75%,#e9e9e9)" role="img" aria-label="Light oak door thumbnail"></div>
<div class="thumb" style="left:239px;background:linear-gradient(90deg,#e6e3de,#d9d3cb 50%,#e8e5e0)" role="img" aria-label="White melamine door thumbnail"></div>
<div class="thumb" style="left:294px;background:linear-gradient(90deg,#f1f1f0,#e2e2e1 50%,#8f9496 55%,#a8abac)" role="img" aria-label="Door edge detail thumbnail"></div>

<nav class="crumb">Home / Doors / Melamine Sliding Doors / Melamine Sliding Doors</nav>
<h1 class="title">Melamine Sliding Doors</h1>
<p class="price"><del>$800.00</del>$750.00</p>

<span class="opt-label" style="left:358px;top:166px">Size</span>
<span class="opt-value" style="left:358px;top:179px">Up to 2400mm (h) x 1200mm (w)</span>
<span class="opt-label" style="left:358px;top:203px">Frame profile option</span>
<span class="opt-value" style="left:358px;top:215px">Slim line<span class="sep">|</span>Groove<span class="sep">|</span>Square Edge</span>
<span class="opt-label" style="left:358px;top:240px">Door frame colour option</span>
<span class="opt-value" style="left:358px;top:252px">White<span class="sep">|</span>Anodised silver</span>
<span class="opt-label" style="left:358px;top:276px">Standard melamine option</span>
<span class="opt-value" style="left:358px;top:288px">Simple White<span class="sep">|</span>Lite Oak<span class="sep">|</span>Dark Oak</span>
<span class="opt-label" style="left:358px;top:313px">Safety mirror option</span>
<span class="opt-value" style="left:358px;top:325px">Silver mirror<span class="sep">|</span>Grey mirror<span class="sep">|</span>Black mirror</span>

<span class="qty">1</span>
<span class="add-cart">Add to cart</span>
<div class="rule" style="left:358px;top:372px;width:193px"></div>
<p class="cats">Categories: <a>Doors</a>, <a>Melamine Sliding Doors</a></p>

<div class="rule" style="left:131px;top:495px;width:420px"></div>
<div class="tab-active"></div>
<span class="tab" style="left:131px">Description</span>
<span class="tab" style="left:176px">Reviews (0)</span>

<span class="opt-label" style="left:131px;top:523px">Size</span>
<span class="opt-value" style="left:131px;top:535px">Up to 2400mm (h) x 1200mm (w)</span>
<span class="opt-label" style="left:131px;top:558px">Frame profile option</span>
<span class="opt-value" style="left:131px;top:570px">Slim line<span class="sep">|</span>Groove<span class="sep">|</span>Square Edge</span>
<span class="opt-label" style="left:131px;top:594px">Door frame colour option</span>
<span class="opt-value" style="left:131px;top:606px">White<span class="sep">|</span>Anodised silver</span>
<span class="opt-label" style="left:131px;top:630px">Standard melamine option</span>
<span class="opt-value" style="left:131px;top:642px">Simple White<span class="sep">|</span>Lite Oak<span class="sep">|</span>Dark Oak</span>
<span class="opt-label" style="left:131px;top:665px">Safety mirror option</span>
<span class="opt-value" style="left:131px;top:677px">Silver mirror<span class="sep">|</span>Grey mirror<span class="sep">|</span>Black mirror</span>

<h2 class="section-title">Related products</h2>

<article class="related" style="left:131px">
  <div class="img" style="background:linear-gradient(90deg,#9aa2a6,#d8cfc4 30%,#6f6a66 55%,#d3c8bb 80%,#c9c3bb)" role="img" aria-label="Bi-fold wardrobe doors in oak and grey"></div>
  <p class="cat">Bi-fold Doors</p><p class="name">Bi-fold Doors</p>
  <p class="stars">☆☆☆☆☆</p><p class="cost"><del>$890.00</del>$765.00</p>
</article>
<article class="related" style="left:238px">
  <div class="img" style="background:linear-gradient(180deg,#d9d9d6 0%,#b6b4b0 40%,#8c6b4f 78%,#6a4a33 100%)" role="img" aria-label="Glass room divider in a study with timber floor"></div>
  <p class="cat">Doors</p><p class="name">Room Divider</p>
  <p class="stars">☆☆☆☆☆</p><p class="cost"><del>$555.00</del>$543.00</p>
</article>
<article class="related" style="left:345px">
  <div class="img" style="background:linear-gradient(90deg,#c8c9c8,#f2f2f1 20%,#ebebea 70%,#b9bcbd)" role="img" aria-label="White hinged wardrobe doors"></div>
  <p class="cat">Doors</p><p class="name">Hinge Doors</p>
  <p class="stars">☆☆☆☆☆</p><p class="cost"><del>$789.00</del>$765.00</p>
</article>
<span class="badge" style="left:209px;top:719px">Sale!</span>
<span class="badge" style="left:316px;top:719px">Sale!</span>
<span class="badge" style="left:423px;top:719px">Sale!</span>

<section class="cta-band">
  <h2>Looking to renovate your wardrobe?</h2>
  <span class="shop-now">SHOP NOW</span>
</section>

<footer class="site-footer"></footer>
<div class="brand" style="left:100px;top:1114px;font-size:16px"><span class="mark" style="width:14px;height:14px"></span>Pantrel</div>

<span class="foot-head" style="left:217px">QUICK LINKS</span>
<span class="foot-link" style="left:217px;top:1087px">Home</span>
<span class="foot-link" style="left:217px;top:1107px">Products</span>
<span class="foot-link" style="left:217px;top:1126px">Gallery</span>
<span class="foot-link" style="left:217px;top:1146px">Buyer's Guide</span>

<span class="foot-head" style="left:345px">PRODUCTS</span>
<span class="foot-link" style="left:345px;top:1087px">Doors</span>
<span class="foot-link" style="left:345px;top:1107px">Wardrobe System</span>
<span class="foot-link" style="left:345px;top:1126px">Storage Space</span>
<span class="foot-link" style="left:345px;top:1146px">Accessories</span>

<span class="foot-head" style="left:473px">OUR BRANCHES</span>
<span class="branch name" style="top:1084px">Auckland Showroom</span>
<span class="branch tel" style="top:1096px">09 555 0142</span>
<span class="branch name" style="top:1108px">Hamilton Showroom</span>
<span class="branch tel" style="top:1121px">07 555 0187</span>

</body>
</html>
```